Dental Lab flyer

I would like eye catching dental lab flyer. Promoting Q.lin , Brevon Zirconia, and 7R Dunor Vistane Zirconia.
Price Q.lin $85
Brevon $44
7R $56

```html
<!DOCTYPE html>
<html lang="en">
<head>
<meta charset="UTF-8">
<title>Crestline Dental Lab Flyer</title>
<link rel="stylesheet" href="https://fonts.googleapis.com/css2?family=Montserrat:wght@400;500;600;700;800&display=swap">
<style>
  :root {
    --brand-blue: #0b3a98;
    --brand-blue-deep: #082d7c;
    --ink-dark: #1d1c20;
    --paper: #ffffff;
    --row-grey: #e6e8ee;
    --photo-light: #eef0f3;
    --photo-skin: #e9c9ae;
  }
  * { margin: 0; padding: 0; box-sizing: border-box; }
  html, body {
    width: 800px; height: 1200px; overflow: hidden;
    background: var(--paper);
    font-family: "Montserrat", sans-serif;
  }
  .flyer {
    position: relative; width: 800px; height: 1200px; overflow: hidden;
    background: var(--brand-blue);
  }
  .hero-photo {
    position: absolute; left: 0; top: 0; width: 800px; height: 720px;
    background:
      radial-gradient(ellipse 260px 220px at 250px 260px, #f0d3bc 0%, rgba(240,211,188,0) 70%),
      radial-gradient(ellipse 300px 160px at 420px 470px, #f3dcc4 0%, rgba(243,220,196,0) 75%),
      radial-gradient(ellipse 200px 300px at 700px 260px, #d9dde3 0%, rgba(217,221,227,0) 75%),
      linear-gradient(160deg, #f4f5f7 0%, var(--photo-light) 55%, #dfe2e7 100%);
  }
  .shapes { position: absolute; left: 0; top: 0; width: 800px; height: 1200px; }
  .feature-photo {
    position: absolute; border-radius: 50%;
    border: 5px solid var(--paper);
    box-shadow: 0 4px 10px rgba(0,0,0,0.18);
  }
  .feature-photo--patient {
    left: 48px; top: 492px; width: 242px; height: 242px;
    background: radial-gradient(circle at 55% 40%, #e8c7b1 0%, #a9c6df 45%, #6f9cc8 100%);
  }
  .feature-photo--model {
    left: 314px; top: 522px; width: 222px; height: 222px;
    background: radial-gradient(circle at 50% 45%, #d9735d 0%, #e6c6c0 40%, #e8eaee 100%);
  }
  .feature-photo--clinic {
    left: 552px; top: 513px; width: 202px; height: 202px;
    background: radial-gradient(circle at 60% 45%, #c9d3e2 0%, #9fb4d4 45%, #dfe4ec 100%);
  }
  .headline {
    position: absolute; left: 50px; top: 776px; width: 400px;
    color: var(--paper); font-size: 38px; font-weight: 700; line-height: 52px;
    letter-spacing: 0.2px;
  }
  .headline__lead { font-weight: 500; }
  .column-rule {
    position: absolute; left: 457px; top: 786px; width: 2px; height: 194px;
    background: var(--paper);
  }
  .price-label {
    position: absolute; left: 502px; top: 794px;
    color: var(--paper); font-size: 26px; font-weight: 700; letter-spacing: 0.5px;
  }
  .price-list { position: absolute; left: 500px; top: 835px; width: 246px; list-style: none; }
  .price-row {
    display: flex; justify-content: space-between; align-items: center;
    height: 36px; margin-bottom: 15px; padding: 0 10px 0 16px;
    border-radius: 6px;
    background: linear-gradient(90deg, var(--row-grey) 0%, var(--row-grey) 72%, var(--paper) 72%);
  }
  .price-row__name { font-size: 15px; font-weight: 600; color: var(--ink-dark); }
  .price-row__amount { font-size: 23px; font-weight: 700; color: var(--brand-blue); }
  .brand {
    position: absolute; left: 40px; top: 1090px; width: 190px;
    display: flex; flex-direction: column; align-items: center; gap: 10px;
  }
  .brand__dot { width: 34px; height: 34px; border-radius: 50%; border: 3px solid var(--paper); }
  .brand__name { color: var(--paper); font-size: 16px; font-weight: 500; letter-spacing: 1.5px; white-space: nowrap; }
  .footer-rule {
    position: absolute; left: 262px; top: 1082px; width: 2px; height: 84px;
    background: var(--paper);
  }
  .visit-label {
    position: absolute; left: 283px; top: 1122px;
    color: var(--paper); font-size: 19px; font-weight: 700;
  }
  .site-link {
    position: absolute; left: 474px; top: 1110px; width: 276px; height: 44px;
    border-radius: 22px; background: var(--brand-blue);
    color: var(--paper); font-size: 18px; font-weight: 700;
    display: flex; align-items: center; justify-content: center;
  }
</style>
</head>
<body>
  <main class="flyer">
    <div class="hero-photo" role="img" aria-label="Photo of a smiling patient reclining in a dental chair while a dentist holds a mouth mirror"></div>

    <svg class="shapes" viewBox="0 0 800 1200" aria-hidden="true">
      <path d="M0 640 C 180 620, 300 700, 480 660 C 620 630, 700 520, 800 512 L800 1200 L0 1200 Z" fill="var(--brand-blue)"/>
      <path d="M0 1074 C 50 1050, 90 1036, 150 1034 C 280 1032, 360 1092, 470 1088 C 600 1084, 700 1040, 800 1046 L800 1200 L0 1200 Z" fill="var(--ink-dark)"/>
    </svg>

    <div class="feature-photo feature-photo--patient" role="img" aria-label="Photo of a dentist examining a patient with an open mouth"></div>
    <div class="feature-photo feature-photo--model" role="img" aria-label="Photo of gloved hands holding a dental model"></div>
    <div class="feature-photo feature-photo--clinic" role="img" aria-label="Photo of a dentist treating a patient in a clinic"></div>

    <h1 class="headline"><span class="headline__lead">Promoting</span> Q.lin Brevon Zirconia, &amp; 7R Dunor Vistane Zirconia</h1>
    <div class="column-rule"></div>

    <h2 class="price-label">PRICE:</h2>
    <ul class="price-list">
      <li class="price-row"><span class="price-row__name">Q.lin</span><span class="price-row__amount">$85</span></li>
      <li class="price-row"><span class="price-row__name">Brevon Zirconia</span><span class="price-row__amount">$44</span></li>
      <li class="price-row"><span class="price-row__name">7R Dunor Vistane</span><span class="price-row__amount">$56</span></li>
    </ul>

    <div class="brand">
      <span class="brand__dot"></span>
      <span class="brand__name">CRESTLINE DENTAL</span>
    </div>
    <div class="footer-rule"></div>
    <p class="visit-label">Please visit us at:</p>
    <p class="site-link">www.crestlinedental.com</p>
  </main>
</body>
</html>
```